RidgeHornSupply.com

I need a new webdesign for a company in the San Jose/SF Bay area that showcases the financial benefits of buying used band instruments for junior high students.This would be opposed to the current and costly option of renting cheap quality instruments from the 2 or 3 local music stores that charge a monthly fee that over the years charges the buyer 3 or 4x over..
Instruments: focus in on Alto Sax, Trumpet, Flute, Clarinet, Trombone, Tenor Sax, Baritone
Target middle schools are Kestrelwood Middle School and Harlow Middle School in San Jose, CA. Both have award winning band programs.
Files attached may or may not be important.
Tabs Needed and funtional
Contact
Shopping Cart
Select Instrument
Checkout
Add to Cart, etc.
Instuments
quantity, etc.
trade in your instrument/sell your instrument
ability to add or take away new instruments for sale. including pictures
Additional questions or info, feel free to ask
Hi Designers,
Project Deadline Extended
Reason: In the next week you will be receiving specific content that will be required to be had on the website.
New desigins are still welcome. Please continue to contact me if you have questions about your individual designs.
Thanks!
Ridge Horn

```html
<!DOCTYPE html>
<html lang="en">
<head>
<meta charset="utf-8">
<title>Ridge Horn Instruments</title>
<link href="https://fonts.googleapis.com/css2?family=Open+Sans:wght@400;600;700&family=Playfair+Display&display=swap" rel="stylesheet">
<style>
:root{
  --gold:#f2c230;
  --gold-deep:#e0a81e;
  --gold-soft:#f7d15a;
  --ink:#111;
  --body:#555;
  --nav:#3a3a3a;
  --page:#f7f7f7;
  --footer:#e6e6e6;
  --line:#d8d8d8;
  --date:#3aa43a;
  --link:#d8334a;
}
*{margin:0;padding:0;box-sizing:border-box}
html,body{width:725px;height:1200px;overflow:hidden}
body{position:relative;background:var(--page);font-family:"Open Sans",Arial,sans-serif;color:var(--ink)}
.abs{position:absolute}
.top-band{left:0;top:0;width:725px;height:334px;background:linear-gradient(135deg,var(--gold-soft),var(--gold) 50%,var(--gold-soft))}
.header{left:110px;top:8px;width:505px;height:57px;background:#fff}
.brand{left:14px;top:14px;display:flex;align-items:center;gap:6px}
.brand-dot{width:12px;height:12px;border-radius:50%;background:var(--gold)}
.brand-name{font-weight:700;font-size:17px;color:#3a3a3a;letter-spacing:.5px}
.brand-sub{left:32px;top:43px;font-size:5px;letter-spacing:3px;color:#333;font-weight:600}
.account{right:9px;top:12px;font-size:5.5px;color:#333}
.cart{left:273px;top:33px;font-size:8px;color:#333}
.cart b{color:#c33;font-weight:400}
.bag{left:320px;top:30px;width:37px;height:14px;border-radius:4px;background:var(--gold);font-size:5.5px;text-align:center;line-height:14px}
.search{left:362px;top:30px;width:136px;height:14px;border:1px solid var(--line);border-radius:4px;font-size:4.6px;color:#aaa;line-height:12px;padding-left:7px}
.search-btn{right:-1px;top:-1px;width:17px;height:14px;border-radius:4px;background:var(--gold)}
.nav{left:106px;top:65px;width:513px;height:17px;background:var(--nav);display:flex;font-size:6px;color:#fff}
.nav a{padding:0 7px;line-height:17px;border-right:1px solid #555;text-decoration:none;color:#fff}
.nav a.current{color:var(--gold)}
.nav .special{margin-left:auto;width:110px;text-align:center;background:linear-gradient(var(--gold),var(--gold-deep));font-weight:700;border:0}
.hero{left:110px;top:86px;width:505px;height:219px;background:linear-gradient(#6f7a5c,#b33 55%,#7a6a58)}
.hero-bar{left:0;bottom:12px;width:505px;height:60px;background:rgba(0,0,0,.45)}
.hero-title{left:98px;top:164px;color:#fff;font-size:11px;line-height:1.1}
.hero-title strong{font-size:16px;display:block}
.hero-btn{left:336px;top:168px;width:62px;height:22px;border:2px solid #fff;color:#fff;font-size:7px;font-weight:700;text-align:center;line-height:18px}
.arrow{top:99px;width:22px;height:22px;border:1.5px solid #fff}
.h2{font-weight:700;font-size:10px}
.copy{font-size:5.4px;line-height:10.5px;color:var(--body)}
.rule{height:1px;background:var(--line)}
.product-img{border:2px solid #ccc;border-radius:3px;width:153px}
.product-title{width:153px;text-align:center;font-size:7px;font-weight:700}
.product-copy{width:153px;text-align:center}
.sidebar{left:460px;top:353px;width:155px;height:716px;border:1px solid #ccc;border-radius:3px;background:#fff}
.ad{left:4px;width:146px;height:112px;background:var(--gold)}
.ad-name{width:100%;text-align:center;font-family:"Playfair Display",serif;font-size:24px;top:20px;color:#333}
.pill{background:#333;color:var(--gold);font-size:5.5px;border-radius:3px;padding:3px 8px}
.ad-url{width:100%;text-align:center;font-size:7px;top:90px;color:#333}
.side-title{width:100%;text-align:center;font-weight:700;font-size:12px}
.social{width:28px;height:28px}
.post{left:7px;width:140px;height:40px}
.post-photo{width:32px;height:32px;background:linear-gradient(#c9c9c9,#8d8d8d)}
.post-body{left:38px;top:0;font-size:5.3px;line-height:8px;color:#333}
.post-body .date{color:var(--date)}
.post-body .more{color:var(--link);text-decoration:underline}
.side-btn{left:52px;top:947px;width:52px;height:14px;border-radius:4px;background:var(--gold);font-size:5.5px;text-align:center;line-height:14px}
.footer{left:0;top:1090px;width:725px;height:110px;background:var(--footer);text-align:center;font-size:6px;color:#333}
.foot-icons{left:345px;top:11px;display:flex;gap:6px}
.foot-icons span{width:8px;height:8px;border-radius:50%;background:#111}
.cards{left:290px;top:49px;display:flex;gap:3px}
.cards span{width:15px;height:9px;background:#c9c9c9;border:1px solid #aaa}
</style>
</head>
<body>
<div class="abs top-band" role="img" aria-label="Gold diamond-patterned background"></div>

<header class="abs header">
  <div class="abs brand"><span class="brand-dot"></span><span class="brand-name">RIDGE HORN</span></div>
  <div class="abs brand-sub">INSTRUMENTS</div>
  <div class="abs account">My account &nbsp;|&nbsp; My wishlist</div>
  <div class="abs cart">
    <svg width="8" height="7" viewBox="0 0 8 7"><path d="M0 1h1.5l1 4h4l1-3H2" fill="none" stroke="#333" stroke-width="1"/><circle cx="3" cy="6.3" r=".7"/><circle cx="6" cy="6.3" r=".7"/></svg>
    $0.00 <b>(0)</b></div>
  <div class="abs bag">MY BAG</div>
  <div class="abs search">FIND A PRODUCT OR BRAND
    <div class="abs search-btn"><svg width="17" height="14" viewBox="0 0 17 14"><circle cx="9" cy="6" r="2.6" fill="none" stroke="#333" stroke-width="1.2"/><path d="M7 8l-2.5 2.5" stroke="#333" stroke-width="1.5"/></svg></div>
  </div>
</header>

<nav class="abs nav">
  <a class="current">HOME</a><a>ABOUT</a><a>WHY RIDGE HORN INSTRUMENTS</a><a>SCHOOLS</a><a>SELL US YOUR USED INSTRUMENT</a><a>FAQ'S</a><a>CONTACT US</a><a class="special">SPECIAL REQUEST</a>
</nav>

<section class="abs hero" role="img" aria-label="Marching band in red and white uniforms holding letter signs">
  <div class="abs hero-bar"></div>
  <div class="abs hero-title" style="left:98px;top:164px">BUY USED BAND INSTRUMENTS FOR<strong>YOUR STUDENT</strong></div>
  <div class="abs hero-btn" style="left:336px;top:168px">READ MORE</div>
  <div class="abs arrow" style="left:13px"><svg width="19" height="19" viewBox="0 0 19 19"><path d="M12 3l-6 6.5 6 6.5" fill="none" stroke="#fff" stroke-width="1.3"/></svg></div>
  <div class="abs arrow" style="right:13px"><svg width="19" height="19" viewBox="0 0 19 19"><path d="M7 3l6 6.5-6 6.5" fill="none" stroke="#fff" stroke-width="1.3"/></svg></div>
</section>

<main>
  <h2 class="abs h2" style="left:110px;top:353px">About Ridge Horn Instruments.</h2>
  <p class="abs copy" style="left:110px;top:373px;width:320px">A company in the San Jose/SF Bay area that showcases the financial benefits of buying used band instruments for junior high students.This would be opposed to the current and costly option of renting cheap quality instruments from the 2 or 3 local music stores that charge a monthly fee that over the years charges the buyer 3 or 4x over..</p>
  <p class="abs copy" style="left:110px;top:414px;width:320px">We target middle schools are Kestrelwood Middle School and Harlow Middle School in San Jose, CA. Both have award winning band programs.</p>
  <div class="abs rule" style="left:110px;top:450px;width:328px"></div>
  <h2 class="abs h2" style="left:109px;top:467px">Our Popular Products.</h2>

  <div class="abs product-img" style="left:113px;top:496px;height:101px;background:linear-gradient(#5a4a30,#1c1c1c)" role="img" aria-label="School band players in a rehearsal"></div>
  <div class="abs product-title" style="left:113px;top:604px">SAXAPHONES</div>
  <p class="abs copy product-copy" style="left:113px;top:622px">Lorem Ipsum is simply dummy text of the printing and typesetting industry. Lorem Ipsum has been the industry's standard dummy text ever since the 1500s</p>

  <div class="abs product-img" style="left:113px;top:665px;height:101px;background:linear-gradient(#a98a52,#5a6b80)" role="img" aria-label="Students playing trombone and horn"></div>
  <div class="abs product-title" style="left:113px;top:773px">CLARINETS</div>
  <p class="abs copy product-copy" style="left:113px;top:791px">Lorem Ipsum is simply dummy text of the printing and typesetting industry. Lorem Ipsum has been the industry's standard dummy text ever since the 1500s</p>

  <div class="abs product-img" style="left:113px;top:833px;height:171px;background:linear-gradient(135deg,#dfe3e8,#7f8a96)" role="img" aria-label="Silver flute lying on sheet music"></div>
  <div class="abs product-title" style="left:113px;top:1011px">FLUTE</div>
  <p class="abs copy product-copy" style="left:113px;top:1029px">Lorem Ipsum is simply dummy text of the printing and typesetting industry. Lorem Ipsum has been the industry's standard dummy text ever since the 1500s</p>

  <div class="abs product-img" style="left:286px;top:496px;height:170px;background:linear-gradient(#2a2a2a,#050505)" role="img" aria-label="Silver trombone on a black background"></div>
  <div class="abs product-title" style="left:286px;top:673px">TENOR SAXAPHONES</div>
  <p class="abs copy product-copy" style="left:286px;top:691px">Lorem ipsum is simply dummy text of the printing and typesetting industry. Lorem Ipsum has been the industry's standard dummy text ever since the 1500s</p>

  <div class="abs product-img" style="left:286px;top:734px;height:101px;background:linear-gradient(135deg,#c4902e,#1a1a1a)" role="img" aria-label="Gold saxophone close-up"></div>
  <div class="abs product-title" style="left:286px;top:842px">TROMBONES AND TRUMPETS</div>
  <p class="abs copy product-copy" style="left:286px;top:860px">Lorem Ipsum is simply dummy text of the printing and typesetting industry. Lorem Ipsum has been the industry's standard dummy text ever since the 1500s</p>
</main>

<aside class="abs sidebar">
  <div class="abs ad" style="top:5px" role="img" aria-label="Trumpet promotion on gold textured background">
    <div class="abs ad-name">TRUMPET</div>
    <div class="abs pill" style="left:50px;top:62px">BUY NOW</div>
    <div class="abs ad-url">www.RidgeHornSupply.com</div>
  </div>
  <div class="abs rule" style="left:4px;top:124px;width:146px"></div>
  <div class="abs ad" style="top:131px;background:linear-gradient(90deg,#3a3a3a 55%,var(--gold) 55%)" role="img" aria-label="Tenor sax promotion with a saxophone player">
    <div class="abs" style="left:16px;top:76px;background:var(--gold);color:#333;font-size:5.5px;border-radius:3px;padding:3px 8px">BUY NOW</div>
  </div>
  <div class="abs rule" style="left:4px;top:249px;width:146px"></div>
  <div class="abs ad" style="top:256px;background:linear-gradient(90deg,#b8952a,var(--gold))" role="img" aria-label="Special request promotion with a tuba player">
    <div class="abs pill" style="left:80px;top:69px">CONTACT NOW</div>
    <div class="abs" style="left:74px;top:89px;font-size:4px;color:#333">www.RidgeHornSupply.com</div>
  </div>
  <div class="abs rule" style="left:4px;top:375px;width:146px"></div>
  <div class="abs side-title" style="top:389px">FOLLOW US</div>
  <div class="abs social" style="left:23px;top:413px;background:#e49a22"></div>
  <div class="abs social" style="left:63px;top:413px;background:#3b5a9a"></div>
  <div class="abs social" style="left:102px;top:413px;background:#27a6de"></div>
  <div class="abs rule" style="left:4px;top:465px;width:146px"></div>
  <div class="abs side-title" style="top:475px">POPULAR POSTS</div>

  <div class="abs post" style="top:504px"><div class="abs post-photo" role="img" aria-label="Author portrait"></div>
    <div class="abs post-body"><span class="date">02/20/2014</span><br>Lorem Ipsum is simply dummy text<br>of the printing and typesetting<br>industry. Lorem...... <span class="more">Read more</span></div></div>
  <div class="abs rule" style="left:7px;top:544px;width:140px"></div>
  <div class="abs post" style="top:552px"><div class="abs post-photo" role="img" aria-label="Author portrait"></div>
    <div class="abs post-body"><span class="date">02/20/2014</span><br>Lorem Ipsum is simply dummy text<br>of the printing and typesetting<br>industry. Lorem...... <span class="more">Read more</span></div></div>
  <div class="abs rule" style="left:7px;top:592px;width:140px"></div>
  <div class="abs post" style="top:600px"><div class="abs post-photo" role="img" aria-label="Author portrait"></div>
    <div class="abs post-body"><span class="date">02/20/2014</span><br>Lorem Ipsum is simply dummy text<br>of the printing and typesetting<br>industry. Lorem...... <span class="more">Read more</span></div></div>
  <div class="abs rule" style="left:7px;top:640px;width:140px"></div>
  <div class="abs post" style="top:648px"><div class="abs post-photo" role="img" aria-label="Author portrait"></div>
    <div class="abs post-body"><span class="date">02/20/2014</span><br>Lorem Ipsum is simply dummy text<br>of the printing and typesetting<br>industry. Lorem...... <span class="more">Read more</span></div></div>
  <div class="abs rule" style="left:7px;top:688px;width:140px"></div>
  <div class="abs side-btn" style="top:693px">READ MORE</div>
</aside>

<footer class="abs footer">
  <div class="abs foot-icons"><span></span><span></span><span></span></div>
  <div class="abs" style="left:0;top:29px;width:725px">Call 0100 2345 678 or email <b>contact@ridgehornsupply.com</b></div>
  <div class="abs cards"><span></span><span></span><span></span><span></span><span></span><span></span><span></span><span></span><span></span><span></span></div>
  <div class="abs" style="left:0;top:70px;width:725px">Home &nbsp;|&nbsp; About &nbsp;|&nbsp; Instuments &nbsp;|&nbsp; Trade in your instrument &nbsp;|&nbsp; Sell your instrument &nbsp;|&nbsp; FAQ's &nbsp;|&nbsp; Contact Us</div>
  <div class="abs" style="left:0;top:84px;width:725px">Copyright 2014 Ridge Horn Instruments</div>
</footer>
</body>
</html>
```